Corvane Health a direct primary care practice needs a beautiful and customer friendly website

We need a website to showcase our new medical practice. We want to enhance the customer experience and make it easy to navigate to the desired page by placing pillar pages on the home screen. the website needs to be clean and bright.

Target Market(s)

Uninsured, Small businesses that can't afford to offer employees insurance.

Industry/Entity Type

Healthcare

Coding

Coded - Design and coding required

Font styles to use
Serif
Sans Serif

Colors
0592cd
3377b5
0355a3
9bcb3c
acd136

Requirements
Must have
• Must be user friendly, must have pillar pages to help boost SEO ranking, clean and bright, must be close to the in colors to the attached logo.

Content will be very similar to www.brisklomacare.example
Nice to have
• Clean and easy to read font

```html
<!DOCTYPE html>
<html lang="en">
<head>
<meta charset="utf-8">
<title>Corvane Health</title>
<link href="https://fonts.googleapis.com/css2?family=Roboto:wght@300;400;500;700&family=Montserrat:wght@600&display=swap" rel="stylesheet">
<style>
:root{
  --green:#8cc63f;
  --green-dark:#7db52f;
  --blue:#0592cd;
  --blue-mid:#1a7bc4;
  --blue-deep:#0b3f95;
  --navy:#1d3f8c;
  --ink:#333;
  --text:#555;
  --white:#fff;
  --black:#000;
}
*{box-sizing:border-box;margin:0;padding:0}
html,body{width:1200px;height:2937px;overflow:hidden}
body{font-family:'Roboto',Arial,sans-serif;color:var(--text);background:var(--white);position:relative}
.abs{position:absolute}
.btn{position:absolute;display:flex;align-items:center;justify-content:center;font-family:'Roboto',Arial,sans-serif;font-weight:500;border-radius:2px;text-decoration:none}

/* header */
.site-header{position:absolute;left:0;top:0;width:1200px;height:105px;background:var(--white)}
.brand{position:absolute;left:114px;top:40px;font-size:26px;font-weight:500;color:var(--navy);line-height:1}
.nav{position:absolute;left:418px;top:46px;display:flex;gap:20px;font-size:13.5px;color:#444}
.nav .active{color:var(--green);border-bottom:3px solid var(--green);padding-bottom:4px}
.join-top{left:1003px;top:39px;width:86px;height:31px;background:var(--green);color:#fff;font-size:13px}

/* hero */
.hero-photo{position:absolute;left:0;top:105px;width:1200px;height:622px;background:linear-gradient(90deg,#0b7dcb 0%,#3c8fd0 30%,#a9bed3 55%,#d3d8df 75%,#e1e3e6 100%)}
.hero h1{position:absolute;left:109px;top:272px;font-size:40px;font-weight:700;color:#fff;line-height:52px}
.hero p{position:absolute;left:112px;top:378px;width:470px;font-size:16.5px;font-weight:500;color:#fff;line-height:25px}
.join-hero{left:112px;top:439px;width:84px;height:31px;background:var(--green);color:#fff;font-size:13px}
.slide-no{position:absolute;left:946px;top:495px;font-size:76px;font-weight:700;color:var(--green);line-height:1}

/* step up */
.section-title{position:absolute;left:0;width:1200px;text-align:center;font-size:31px;font-weight:400;color:#444}
.section-title span{color:var(--blue-mid)}
.section-sub{position:absolute;left:350px;width:500px;text-align:center;font-size:16px;line-height:24px;color:#555}
.rule{position:absolute;left:562px;width:76px;height:3px;background:var(--blue-mid)}
.intro-text{position:absolute;left:112px;top:878px;width:415px;font-size:13.5px;line-height:24px;color:#555}
.intro-text p+p{margin-top:24px}
.learn-blue{left:112px;top:1140px;width:107px;height:30px;background:var(--blue-mid);color:#fff;font-size:13.5px}
.video{position:absolute;left:598px;top:883px;width:491px;height:249px;background:linear-gradient(120deg,#7a5d4c,#b59a8a 45%,#d8c2b8 70%,#9b8b86);box-shadow:0 2px 6px rgba(0,0,0,.35)}

/* benefits */
.benefits-bg{position:absolute;left:0;top:1233px;width:1200px;height:705px;background:linear-gradient(180deg,#e7eef5 0%,#eef3f8 55%,#ffffff 100%)}
.benefits-copy{position:absolute;left:222px;top:1430px;width:758px;text-align:center;font-size:13.5px;line-height:24px;color:#555}
.card{position:absolute;top:1569px;width:321px;height:288px;color:#fff;text-align:center}
.card.green{left:112px;background:var(--green)}
.card.navy{left:439px;background:var(--blue-deep)}
.card.blue{left:766px;background:var(--blue-mid)}
.card-head{position:absolute;top:22px;left:0;width:100%;height:56px;display:flex;align-items:center;justify-content:center;gap:20px}
.card-head .bar{width:2px;height:50px;background:#fff}
.card-head h3{font-size:16px;font-weight:500;letter-spacing:.3px}
.card p{position:absolute;left:22px;top:100px;width:277px;font-size:13px;font-weight:500;line-height:20px}
.card .hours{line-height:26px}
.card .btn{left:102px;top:239px;width:116px;height:29px;background:#fff;font-size:16px;font-weight:400}
.card.green .btn{color:var(--green-dark)}
.card.navy .btn{color:var(--blue-deep)}
.card.blue .btn{color:var(--blue-mid)}

/* contact */
.contact-photo{position:absolute;left:0;top:1938px;width:1200px;height:560px;background:linear-gradient(90deg,#3d76c4 0%,#4c86cc 45%,#5a8fd0 100%)}
.contact-title{position:absolute;left:0;top:1994px;width:1200px;text-align:center;font-size:30px;font-weight:700;color:#fff}
.contact-sub{position:absolute;left:270px;top:2033px;width:660px;text-align:center;font-size:15.5px;line-height:27px;color:#fff}
.contact-card{position:absolute;left:112px;top:2135px;width:977px;height:484px;background:#fff;border-bottom:3px solid var(--blue-deep);box-shadow:0 2px 6px rgba(0,0,0,.12)}
.kicker{position:absolute;font-size:21px;letter-spacing:2.5px;color:var(--blue-mid);font-weight:400}
.tagline{position:absolute;left:35px;top:150px;font-size:29px;line-height:36px;font-weight:500;color:var(--blue-mid)}
.address{position:absolute;left:35px;top:235px;font-size:16.5px;line-height:27px;color:var(--blue-mid)}
.help-phone{position:absolute;left:153px;top:365px;font-size:30px;font-weight:500;color:var(--blue-mid)}
.field{position:absolute;border:1px solid #cfcfcf;background:#fff;font-size:12px;color:#888;padding:14px 16px}
.submit{left:476px;top:322px;width:204px;height:45px;background:var(--green);color:#fff;font-family:'Montserrat',Arial,sans-serif;font-weight:600;font-size:18px;border-radius:2px}

/* footer */
.site-footer{position:absolute;left:0;top:2707px;width:1200px;height:230px;background:var(--black);color:#fff}
.footer-brand{position:absolute;left:112px;top:86px;font-size:30px;font-weight:500;color:#fff;line-height:1}
.socials{position:absolute;left:954px;top:82px;display:flex;gap:9px}
.socials span{width:27px;height:27px;border-radius:50%;background:#fff}
.footer-nav{position:absolute;right:112px;top:128px;font-size:14px;font-weight:500;white-space:nowrap}
.footer-nav i{font-style:normal;margin:0 9px}
.copyright{position:absolute;right:112px;top:162px;font-size:14px}
</style>
</head>
<body>

<header class="site-header">
  <div class="brand">Corvane Health</div>
  <nav class="nav">
    <span class="active">HOME</span><span>ABOUT</span><span>SERVICES</span><span>EMPLOYERS</span><span>PRICING</span><span>FAQ</span><span>CONTACT US</span><span>BLOG</span>
  </nav>
  <a class="btn join-top">JOIN US</a>
</header>

<section class="hero">
  <div class="hero-photo" role="img" aria-label="Smiling doctor holding a laughing toddler in a bright clinic"></div>
  <h1>EXPECT MORE<br>FROM YOUR DOCTOR</h1>
  <p>Neque porro quisquam est qui dolorem ipsum quia dolor sit amet, consectetur, adipisci velit...</p>
  <a class="btn join-hero">JOIN US</a>
  <svg class="abs" style="left:580px;top:527px" width="42" height="70" viewBox="0 0 42 70"><rect x="2" y="2" width="38" height="66" rx="19" fill="none" stroke="#fff" stroke-width="2.5"/><circle cx="21" cy="21" r="9" fill="#8cc63f"/></svg>
  <div class="slide-no">01</div>
  <svg class="abs" style="left:1036px;top:523px" width="52" height="30" viewBox="0 0 52 30"><path d="M2 15H48M36 4L48 15 36 26" fill="none" stroke="#fff" stroke-width="3"/></svg>
  <svg class="abs" style="left:0;top:615px" width="1200" height="115" viewBox="0 0 1200 115"><path d="M0 112C250 40 430 5 600 5S950 40 1200 112V115H0Z" fill="#8cc63f"/><path d="M0 115C250 70 430 45 600 45S950 70 1200 115Z" fill="#fff"/></svg>
</section>

<section class="step-up">
  <h2 class="section-title" style="top:720px">Take <span>A Step Up</span></h2>
  <p class="section-sub" style="top:770px">Neque porro quisquam est qui dolorem ipsum quia dolor sit amet, consectetur, adipisci velit...</p>
  <div class="rule" style="top:842px"></div>
  <div class="intro-text">
    <p>Lorem Ipsum is simply dummy text of the printing and typesetting industry. Lorem Ipsum has been the industry's standard dummy text ever since the 1500s, when an unknown printer took a galley of type and scrambled it to make a type specimen book.</p>
    <p>It has survived not only five centuries, but also the leap into electronic typesetting, remaining essentially unchanged. It was popularised in the 1960s with the release of Typeleaf sheets containing Lorem Ipsum passages, and more recently with desktop publishing software like Quillset Composer including versions of Lorem Ipsum.</p>
  </div>
  <a class="btn learn-blue">Learn More</a>
  <div class="video" role="img" aria-label="Video still of a smiling mother and daughter"></div>
  <svg class="abs" style="left:802px;top:966px" width="84" height="84" viewBox="0 0 84 84"><circle cx="42" cy="42" r="39" fill="none" stroke="#fff" stroke-width="3"/><path d="M34 27L58 42 34 57Z" fill="none" stroke="#fff" stroke-width="3" stroke-linejoin="round"/></svg>
</section>

<section class="benefits">
  <div class="benefits-bg" role="img" aria-label="Faded photo of a smiling medical team"></div>
  <h2 class="section-title" style="top:1281px">Benefits Of <span>Our Primary Care Clinic</span></h2>
  <p class="section-sub" style="top:1331px">Neque porro quisquam est qui dolorem ipsum quia dolor sit amet, consectetur, adipisci velit...</p>
  <div class="rule" style="top:1402px"></div>
  <p class="benefits-copy">Lorem Ipsum is simply dummy text of the printing and typesetting industry. Lorem Ipsum has been the industry's standard dummy text ever since the 1500s, when an unknown printer took a galley of type and scrambled it to make a type specimen book. It has survived not only five centuries, but also the leap into electronic typesetting, remaining essentially unchanged. It was popularised in the 1960s with the release of Typeleaf sheets containing Lorem Ipsum passages, and more recently with desktop publishing software like Quillset Composer including versions of Lorem Ipsum.</p>

  <div class="card green">
    <div class="card-head">
      <svg width="66" height="62" viewBox="0 0 66 62" fill="none" stroke="#fff" stroke-width="2.5"><circle cx="38" cy="14" r="11"/><path d="M38 9l1.6 3.4 3.6.4-2.7 2.4.8 3.6-3.3-1.9-3.3 1.9.8-3.6-2.7-2.4 3.6-.4Z" fill="#fff" stroke="none"/><path d="M33 24l-3 10 5-2 3 4 M43 24l3 10-5-2-3 4"/><rect x="3" y="38" width="8" height="20" fill="#fff"/><path d="M11 42h14c4 0 6 3 10 3h8c3 0 3 4 0 4H30 M11 55h24l24-12c3-2 0-6-3-4l-13 6"/></svg>
      <span class="bar"></span><h3>BENEFITS</h3>
    </div>
    <p>It is a long established fact that a reader will be distracted by the readable content of a page when looking at its layout. The point of using Lorem Ipsum is that it has a more-or-less normal distribution of letters, as opposed to using</p>
    <a class="btn">Learn More</a>
  </div>

  <div class="card navy">
    <div class="card-head">
      <svg width="74" height="54" viewBox="0 0 74 54"><path d="M26 4C12 4 3 12 3 22c0 6 3 11 8 14l-2 10 10-7c2 .5 4 .7 7 .7 14 0 23-8 23-18S40 4 26 4Z" fill="#fff"/><circle cx="15" cy="22" r="3" fill="#0b3f95"/><circle cx="26" cy="22" r="3" fill="#0b3f95"/><circle cx="37" cy="22" r="3" fill="#0b3f95"/><circle cx="57" cy="30" r="14" fill="#0b3f95" stroke="#fff" stroke-width="2.5"/><text x="57" y="37" text-anchor="middle" font-family="Roboto,Arial,sans-serif" font-size="19" font-weight="700" fill="#fff">?</text></svg>
      <span class="bar"></span><h3>QUESTIONS?</h3>
    </div>
    <p>It is a long established fact that a reader will be distracted by the readable content of a page when looking at its layout. The point of using Lorem Ipsum is that it has a more-or-less normal distribution of letters, as opposed to using</p>
    <a class="btn">Learn More</a>
  </div>

  <div class="card blue">
    <div class="card-head">
      <svg width="66" height="62" viewBox="0 0 66 62" fill="none" stroke="#fff" stroke-width="3"><circle cx="33" cy="31" r="27"/><circle cx="33" cy="31" r="19" stroke-width="2"/><path d="M24 31l7 7 13-14"/></svg>
      <span class="bar"></span><h3>OFFICE HOURS</h3>
    </div>
    <p class="hours">MWF 9:00 AM – 5:00 PM<br>T/Th 8:00 AM - 4:00 PM<br>Call or text us today at<br>555-318-4072<br>For our members, we are always on call.</p>
    <a class="btn">Book Now</a>
  </div>
</section>

<section class="contact">
  <div class="contact-photo" role="img" aria-label="Blue-toned photo of a smiling nurse"></div>
  <svg class="abs" style="left:0;top:2480px" width="1200" height="100" viewBox="0 0 1200 100"><path d="M0 90C40 60 80 40 112 30V100H0Z M1200 90C1160 60 1120 40 1089 30V100H1200Z" fill="#8cc63f"/></svg>
  <h2 class="contact-title">Contact Us</h2>
  <p class="contact-sub">Lorem Ipsum is simply dummy text of the printing and typesetting industry. Lorem Ipsum has been the industry's standard dummy text ever since the 1500s, when</p>

  <div class="contact-card">
    <svg class="abs" style="left:35px;top:40px" width="50" height="50" viewBox="0 0 50 50"><rect x="10" y="2" width="30" height="30" fill="#8cc63f"/><path d="M15 10h20M15 16h20M15 22h14" stroke="#fff" stroke-width="2"/><path d="M2 20L25 36 48 20V48H2Z" fill="#8cc63f"/><path d="M2 48L20 32M48 48L30 32" stroke="#fff" stroke-width="2"/></svg>
    <div class="kicker" style="left:35px;top:112px">GET IN TOUCH</div>
    <div class="tagline">For our members,<br>we are on call 24/7.</div>
    <div class="address">742 Juniper Ridge Lane,<br>HALVERN, Ostera, 40517.</div>
    <svg class="abs" style="left:42px;top:320px" width="92" height="92" viewBox="0 0 92 92" fill="none" stroke="#8cc63f" stroke-width="2.5"><path d="M8 30c0-14 18-22 38-22s38 8 38 22l-12 4-4-10c-14-4-30-4-44 0l-4 10Z"/><path d="M22 40h48l10 40H12Z"/><circle cx="46" cy="60" r="12"/><circle cx="46" cy="60" r="4"/></svg>
    <div class="kicker" style="left:153px;top:337px">NEED A HELP</div>
    <div class="help-phone">+555-318-4072</div>

    <div class="field" style="left:479px;top:40px;width:229px;height:41px">Name</div>
    <div class="field" style="left:713px;top:40px;width:229px;height:41px">Phone</div>
    <div class="field" style="left:479px;top:108px;width:229px;height:41px">Email</div>
    <div class="field" style="left:713px;top:108px;width:229px;height:41px">Subject</div>
    <svg class="abs" style="left:913px;top:124px" width="18" height="10" viewBox="0 0 18 10"><path d="M0 0H18L9 10Z" fill="#8cc63f"/></svg>
    <div class="field" style="left:479px;top:175px;width:463px;height:114px">Your Message Here</div>
    <a class="btn submit">Submit Now</a>
  </div>
</section>

<footer class="site-footer">
  <div class="footer-brand">Corvane Health</div>
  <div class="socials"><span></span><span></span><span></span><span></span></div>
  <div class="footer-nav">HOME<i>|</i>ABOUT<i>|</i>SERVICES<i>|</i>EMPLOYERS<i>|</i>PRICING<i>|</i>FAQ<i>|</i>CONTACT US<i>|</i>BLOG</div>
  <div class="copyright">Copyright © 2020 Corvane Health. | All Rights Reserved</div>
</footer>

</body>
</html>
```